Gift Card/voucher Design for Beauty Clinic

I need a design for a gift card I Can use in all seasons for my Aesthetic clinic. The Logo is attached. The main colors we use are white and black, we are open for new suggestions to make an friendly yet professional impression. Ideally the gift card/voucher would be foldable.
The inside should contain the following fields:

Für:

Von:

Wert

Gültigkeit

```html
<!DOCTYPE html>
<html lang="de">
<head>
<meta charset="utf-8">
<title>Gift Card and Voucher – Mara Lindqvist Aesthetics</title>
<link rel="stylesheet" href="https://fonts.googleapis.com/css2?family=Bodoni+Moda:wght@400;500&family=Raleway:wght@600&display=swap">
<style>
  :root {
    --sand: #d1c7b4;
    --mint: #b2ddd7;
    --ink: #121212;
    --rule: #4a4a4a;
    --paper: #ffffff;
    --serif: "Bodoni Moda", "Didot", serif;
    --sans: "Raleway", "Helvetica Neue", sans-serif;
  }
  * { box-sizing: border-box; margin: 0; padding: 0; }
  html, body { width: 916px; height: 1200px; overflow: hidden; background: var(--paper); }
  .sheet { position: relative; width: 916px; height: 1200px; background: var(--paper); }

  .card {
    position: absolute;
    width: 323px; height: 187px;
    border-radius: 16px;
  }
  .sand { background: var(--sand); }
  .mint { background: var(--mint); }

  .caption {
    position: absolute;
    transform: translateX(-50%);
    font-family: var(--sans);
    font-weight: 600;
    font-size: 13.5px;
    color: var(--ink);
    white-space: nowrap;
  }

  .brand-name {
    position: absolute;
    left: 50%;
    transform: translate(-50%, -50%);
    font-family: var(--serif);
    font-weight: 500;
    color: var(--ink);
    text-align: center;
    text-transform: uppercase;
    white-space: nowrap;
    line-height: 1.7;
  }
  .brand-name.large { font-size: 11px; letter-spacing: 2px; }
  .brand-name.medium { font-size: 9px; letter-spacing: 1.6px; }
  .brand-name.tiny { font-size: 4.2px; letter-spacing: 0.6px; line-height: 1.5; }
  .card-front .brand-name { top: 50%; }

  .field-list { position: absolute; left: 20px; right: 21px; top: 14px; }
  .field {
    display: block;
    height: 31px;
    padding-top: 3px;
    border-bottom: 0.8px solid var(--rule);
    font-family: var(--serif);
    font-size: 14px;
    color: var(--ink);
    letter-spacing: 0.3px;
  }
  .field + .field { margin-top: 0; }
  .field-list .field:first-child { height: 22px; padding-top: 0; }

  .tagline {
    position: absolute;
    left: 0; right: 0; top: 144px;
    text-align: center;
    font-family: var(--serif);
    font-size: 7.5px;
    letter-spacing: 2.6px;
    color: var(--ink);
  }
  .card-back .brand-name { top: 170px; }

  .voucher {
    position: absolute;
    width: 809px; height: 255px;
  }
  .voucher .fold {
    position: absolute;
    left: 404px; top: 0; bottom: 0;
    width: 0.6px;
    background: rgba(0,0,0,0.06);
  }
  .voucher-cover .brand-name { left: 202px; top: 138px; }
  .seal {
    position: absolute;
    left: 581px; top: 180px;
    width: 51px; height: 51px;
    background: var(--paper);
  }
  .seal .brand-name { top: 50%; }
</style>
</head>
<body>
<main class="sheet">

  <!-- Gift cards: front -->
  <section class="card card-front sand" style="left:115px; top:34px;">
    <p class="brand-name large">Mara Lindqvist<br>Aesthetics</p>
  </section>
  <p class="caption" style="left:282px; top:237px;">FRONT OF THE CARD 1</p>

  <section class="card card-front mint" style="left:479px; top:32px;">
    <p class="brand-name large">Mara Lindqvist<br>Aesthetics</p>
  </section>
  <p class="caption" style="left:646px; top:235px;">FRONT OF THE CARD 2</p>

  <!-- Gift cards: back -->
  <section class="card card-back sand" style="left:121px; top:276px;">
    <div class="field-list">
      <span class="field">Für:</span>
      <span class="field">Von:</span>
      <span class="field">Wert:</span>
      <span class="field">Gültigkeit:</span>
    </div>
    <p class="tagline">VON HERZEN FÜR DICH</p>
    <p class="brand-name tiny">Mara Lindqvist<br>Aesthetics</p>
  </section>
  <p class="caption" style="left:288px; top:479px;">BACK OF THE CARD 1</p>

  <section class="card card-back mint" style="left:485px; top:274px;">
    <div class="field-list">
      <span class="field">Für:</span>
      <span class="field">Von:</span>
      <span class="field">Wert:</span>
      <span class="field">Gültigkeit:</span>
    </div>
    <p class="tagline">VON HERZEN FÜR DICH</p>
    <p class="brand-name tiny">Mara Lindqvist<br>Aesthetics</p>
  </section>
  <p class="caption" style="left:652px; top:477px;">BACK OF THE CARD 2</p>

  <!-- Folding voucher 1 -->
  <section class="voucher voucher-cover sand" style="left:54px; top:539px;">
    <p class="brand-name medium">Mara Lindqvist<br>Aesthetics</p>
    <span class="fold"></span>
    <div class="seal"><p class="brand-name tiny">Mara Lindqvist<br>Aesthetics</p></div>
  </section>
  <p class="caption" style="left:270px; top:824px;">FRONT OF THE VOUCHER 1</p>
  <p class="caption" style="left:665px; top:819px;">BACK OF THE VOUCHER 1</p>

  <!-- Folding voucher 2 -->
  <section class="voucher voucher-cover mint" style="left:57px; top:871px;">
    <p class="brand-name medium">Mara Lindqvist<br>Aesthetics</p>
    <div class="seal"><p class="brand-name tiny">Mara Lindqvist<br>Aesthetics</p></div>
  </section>
  <p class="caption" style="left:274px; top:1156px;">FRONT OF THE VOUCHER 2</p>
  <p class="caption" style="left:669px; top:1151px;">BACK OF THE VOUCHER 2</p>

</main>
</body>
</html>
```